Marlowe Fen Gin (bottle label)

Marlowe Fen Gin is a hand crafted spirit distilled by Tidewell Distillery. The distillery is farm based. This is our first offering. The label is to be applied to a glass bottle.

We chose the name because we felt lucky to chance upon a great recipe. So we came up with Marlowe Fen Gin. The phrase "Sometimes you get lucky" needs to be included. We'd like to see imagery of a lucky symbol such as a 4 leaf clover or shooting star. Elegant contrast come to mind. Reference to the distillery, bottle size (375ml) and Alc./vol. 40% is also needed. The distillery logo could be included. Or all is included in printed content.
Logo included for reference.
The label is rectangular.

Target Market(s)

Adults who enjoy fine spirits

Industry/Entity Type

Spirits distillation

Font styles to use
Serif
Script

Requirements
Must have
• classy, eye catching presentation
Nice to have
• Stylized 4 leaf clover or shooting star
Should not have
• Nothing hokey

```html
<!DOCTYPE html>
<html lang="en">
<head>
<meta charset="utf-8">
<title>Marlowe Fen Gin – Bottle Label</title>
<link rel="stylesheet" href="https://fonts.googleapis.com/css2?family=Cormorant+Garamond:wght@600;700&family=Montserrat:wght@500;600&family=Tinos&display=swap">
<style>
  :root {
    --page: #ffffff;
    --label-black: #070707;
    --frame-silver: #c9cacc;
    --gold-light: #f3d48a;
    --gold-mid: #d6a54e;
    --gold-deep: #a8762b;
    --clover-green: #1f6b2c;
    --clover-dark: #0c2a12;
    --ink-white: #f4f4f2;
    --tag-bg: #1d2a35;
    --tag-edge: #3a4a58;
  }
  * { margin: 0; padding: 0; box-sizing: border-box; }
  html, body {
    width: 1200px; height: 1200px; overflow: hidden;
    background: var(--page);
  }
  .canvas {
    position: relative; width: 1200px; height: 1200px;
    display: flex; align-items: center; justify-content: center;
  }
  .label {
    position: relative; width: 880px; height: 975px;
    background: var(--label-black);
  }
  .label-frame {
    position: absolute; inset: 10px;
    border: 3px solid var(--frame-silver);
  }
  .distillery-name {
    position: absolute; top: 104px; left: 0; right: 0;
    text-align: center;
    font-family: "Cormorant Garamond", serif; font-weight: 600;
    font-size: 34px; letter-spacing: 1px; color: var(--ink-white);
  }
  .lucky-artwork {
    position: absolute; left: 150px; top: 235px; width: 560px; height: 600px;
    border-radius: 46% 46% 40% 40%;
    background:
      radial-gradient(ellipse at 50% 45%, var(--clover-green) 0%, #164d20 40%, var(--clover-dark) 65%, rgba(7,7,7,0) 74%),
      radial-gradient(ellipse at 50% 45%, rgba(214,165,78,0.35) 60%, rgba(7,7,7,0) 76%);
  }
  .product-name {
    position: absolute; top: 440px; left: 0; right: 0;
    text-align: center;
    font-family: "Cormorant Garamond", serif; font-weight: 700;
    font-size: 150px; line-height: 1; letter-spacing: -1px;
    background: linear-gradient(180deg, var(--gold-light) 0%, var(--gold-mid) 55%, var(--gold-deep) 100%);
    -webkit-background-clip: text; background-clip: text; color: transparent;
  }
  .spirit-type {
    position: absolute; top: 686px; left: 0; right: 0;
    text-align: center;
    font-family: "Montserrat", sans-serif; font-weight: 600;
    font-size: 74px; letter-spacing: 2px; color: var(--ink-white);
  }
  .label-footer {
    position: absolute; left: 28px; right: 28px; bottom: 42px;
    display: flex; align-items: center; justify-content: space-between;
  }
  .volume, .strength {
    font-family: "Tinos", serif; font-size: 23px; color: var(--ink-white);
    width: 110px;
  }
  .strength { text-align: right; }
  .tagline {
    background: var(--tag-bg); border: 1px solid var(--tag-edge);
    padding: 4px 14px;
    font-family: "Montserrat", sans-serif; font-weight: 500;
    font-size: 27px; color: var(--ink-white); letter-spacing: 0.3px;
  }
</style>
</head>
<body>
<main class="canvas">
  <section class="label">
    <div class="label-frame"></div>
    <div class="distillery-name">Tidewell Distillery</div>
    <div class="lucky-artwork" role="img" aria-label="Illustration of an ornate gold-edged green four leaf clover against a starry night sky with blue shooting stars"></div>
    <h1 class="product-name">Marlowe Fen</h1>
    <div class="spirit-type">GIN</div>
    <div class="label-footer">
      <span class="volume">375 ml</span>
      <span class="tagline">SOMETIMES YOU GET LUCKY</span>
      <span class="strength">40% abv</span>
    </div>
  </section>
</main>
</body>
</html>
```